I need a flyer made , the flyer can be one page or two pages or three pages . I will be posting this on Instagram and social media platforms. I am a luxury home builder , I am looking to hire a construction project manager . Below are some examples and ideas what can be on the flyer

We’re looking for a construction project manager who’s passionate about building luxury homes at the highest standards
We’re hiring construction project manager
* Experience 5+ years in residential project management with a strong portfolio of completed homes.
* location : Bergen County NJ
* excellent leadership skills, leads teams with confidence and clarity
* communicates seamlessly with architects , engineers, designers and clients
*knows how to manage budgets and timelines without compromising quality
*solves problems with a positive solution first mindset
* pays attention to every detail because in luxury the small things are the big things

Apply now , link in bio or DM to connect.

My logo is attached, my web site www.ridgelanebuilders.com
My style is modern but still warm and inviting. I like a clean classy look .
Updates

Please don’t add any images of chairs or people to the flyer , I do not want people on my flyer. Do not add standard images of offices and houses , we are luxury builders , we build homes over 2 million dollars. Keep a classy , simple modern look . High end .

You can add a white hard hat with my logo on it for a image , this is a suggestion does not have to be on my flyer ,

```html
<!DOCTYPE html>
<html lang="en">
<head>
<meta charset="utf-8">
<title>Ridgelane Builders – Hiring Carousel</title>
<link href="https://fonts.googleapis.com/css2?family=Montserrat:wght@400;500;600;700;800&display=swap" rel="stylesheet">
<style>
  :root{
    --canvas:#d4d5d7;
    --navy:#0f2c5e;
    --navy-deep:#0b2452;
    --blue-mid:#24508a;
    --blue-light:#6d93c0;
    --white:#ffffff;
    --ink:#3a3d42;
    --grey-text:#4a4d52;
    --orange:#f7931e;
    --red-orange:#ea4335;
    --tick:#f5a524;
  }
  *{box-sizing:border-box;margin:0;padding:0}
  html,body{width:1200px;height:865px;overflow:hidden;background:var(--canvas);font-family:"Montserrat",sans-serif}
  .board{position:relative;width:1200px;height:865px}

  .slide-label{position:absolute;top:67px;width:208px;height:42px;border:1px solid #555;border-radius:21px;
    display:flex;align-items:center;justify-content:center;font-weight:700;font-size:25px;color:#3c3c3c;letter-spacing:-0.5px}
  .slide-label--one{left:228px}
  .slide-label--two{left:785px}

  .post{position:absolute;top:169px;width:544px;height:544px;overflow:hidden;
    background:linear-gradient(100deg,var(--navy-deep) 0%,var(--navy) 35%,var(--blue-mid) 70%,var(--blue-light) 100%);
    box-shadow:0 22px 22px -14px rgba(0,0,0,.45)}
  .post--one{left:44px}
  .post--two{left:607px}

  .scene{position:absolute;right:0;top:0;width:300px;height:470px;
    background:linear-gradient(200deg,rgba(140,170,210,.55) 0%,rgba(60,100,160,.35) 45%,rgba(15,44,94,0) 100%)}
  .worker{position:absolute;left:262px;top:59px;width:222px;height:453px;border-radius:60px 60px 10px 10px;
    background:linear-gradient(180deg,rgba(240,150,60,.35) 0%,rgba(60,100,170,.45) 55%,rgba(40,70,130,.4) 100%)}

  .brand{position:absolute;color:var(--white);font-weight:500;font-size:17px;letter-spacing:1px;text-transform:uppercase}
  .post--one .brand{left:63px;top:46px}
  .post--two .brand{left:47px;top:50px}

  .headline{position:absolute;left:61px;top:118px;color:var(--white);line-height:.98}
  .headline__top{display:block;font-weight:800;font-size:64px;letter-spacing:-1px}
  .headline__bottom{display:block;font-weight:500;font-size:68px;letter-spacing:-1px}

  .role{position:absolute;left:61px;top:285px;color:var(--white)}
  .role__title{font-weight:700;font-size:19px;line-height:1.15}
  .role__name{font-weight:400;font-size:19px;line-height:1.15}
  .role__detail{font-weight:400;font-size:15px;margin-top:5px}

  .apply{position:absolute;color:var(--white);font-weight:700;line-height:1;
    background:linear-gradient(120deg,var(--orange) 0%,var(--red-orange) 100%);border-radius:16px 16px 16px 0;
    box-shadow:4px 6px 12px rgba(0,0,0,.3)}
  .post--one .apply{left:61px;top:368px;width:100px;height:69px;font-size:21px;padding:14px 0 0 18px;border-radius:0 18px 18px 0}
  .post--two .apply{left:351px;top:409px;width:131px;height:90px;font-size:28px;padding:17px 0 0 27px;border-radius:20px 0 20px 0}

  .connect{position:absolute;font-size:11px;font-weight:400}
  .post--one .connect{left:61px;top:444px;color:var(--white)}
  .post--two .connect{left:351px;top:511px;color:var(--grey-text);font-size:12px}

  .footer-wave{position:absolute;left:0;bottom:0;width:544px;height:90px}
  .website{position:absolute;left:64px;top:512px;font-size:11.5px;font-weight:500;color:var(--ink)}

  .requirements{position:absolute;left:44px;top:130px;color:var(--white)}
  .requirements__title{font-weight:700;font-size:20px;letter-spacing:.2px}
  .requirements__rule{width:60px;height:1.5px;background:var(--white);margin-top:6px}
  .req-list{list-style:none;position:absolute;left:60px;top:183px;color:var(--white);font-size:11.2px;line-height:15px}
  .req-list li{position:absolute;left:0;padding-left:14px;white-space:nowrap}
  .req-list li svg{position:absolute;left:0;top:2px;width:10px;height:10px}
</style>
</head>
<body>
<main class="board">
  <div class="slide-label slide-label--one">SLIDE 1</div>
  <div class="slide-label slide-label--two">SLIDE 2</div>

  <!-- Slide 1 -->
  <section class="post post--one">
    <div class="scene" role="img" aria-label="Photo of a modern luxury home exterior with glass balconies"></div>
    <div class="worker" role="img" aria-label="Photo of a construction worker in hard hat and safety vest holding a toolbox and clipboard"></div>
    <div class="brand">Ridgelane Builders</div>
    <h1 class="headline"><span class="headline__top">We’re</span><span class="headline__bottom">Hiring</span></h1>
    <div class="role">
      <p class="role__title">Construction</p>
      <p class="role__name">Project Manager</p>
      <p class="role__detail">for Luxury Homes</p>
    </div>
    <div class="apply">Apply<br>Now!</div>
    <p class="connect">link in bio or DM to connect</p>
    <svg class="footer-wave" viewBox="0 0 544 90" preserveAspectRatio="none"><path d="M0 69 C10 48 28 40 51 37 L544 0 L544 90 L0 90 Z" fill="#fff"/></svg>
    <p class="website">www.ridgelanebuilders.com</p>
  </section>

  <!-- Slide 2 -->
  <section class="post post--two">
    <div class="scene" role="img" aria-label="Photo of a modern luxury home exterior with glass balconies and patio"></div>
    <div class="brand">Ridgelane Builders</div>
    <div class="requirements">
      <h2 class="requirements__title">Requirements :</h2>
      <div class="requirements__rule"></div>
    </div>
    <ul class="req-list">
      <li style="top:0">
        <svg viewBox="0 0 10 10"><circle cx="5" cy="5" r="4.2" fill="none" stroke="#f5a524" stroke-width="1.1"/><path d="M3 5.1 L4.6 6.6 L8.6 2.2" fill="none" stroke="#f5a524" stroke-width="1.2"/></svg>
        Experience 5+ years in residential project management<br>with a strong portfolio of completed homes.</li>
      <li style="top:39px">
        <svg viewBox="0 0 10 10"><circle cx="5" cy="5" r="4.2" fill="none" stroke="#f5a524" stroke-width="1.1"/><path d="M3 5.1 L4.6 6.6 L8.6 2.2" fill="none" stroke="#f5a524" stroke-width="1.2"/></svg>
        location : Bergen County, NJ</li>
      <li style="top:59px">
        <svg viewBox="0 0 10 10"><circle cx="5" cy="5" r="4.2" fill="none" stroke="#f5a524" stroke-width="1.1"/><path d="M3 5.1 L4.6 6.6 L8.6 2.2" fill="none" stroke="#f5a524" stroke-width="1.2"/></svg>
        excellent leadership skills, leads teams with confidence and clarity</li>
      <li style="top:79px;line-height:20px">
        <svg viewBox="0 0 10 10"><circle cx="5" cy="5" r="4.2" fill="none" stroke="#f5a524" stroke-width="1.1"/><path d="M3 5.1 L4.6 6.6 L8.6 2.2" fill="none" stroke="#f5a524" stroke-width="1.2"/></svg>
        communicates seamlessly with architects , engineers, designers<br>and clients</li>
      <li style="top:120px">
        <svg viewBox="0 0 10 10"><circle cx="5" cy="5" r="4.2" fill="none" stroke="#f5a524" stroke-width="1.1"/><path d="M3 5.1 L4.6 6.6 L8.6 2.2" fill="none" stroke="#f5a524" stroke-width="1.2"/></svg>
        knows how to manage budgets and timelines without<br>compromising quality</li>
      <li style="top:159px">
        <svg viewBox="0 0 10 10"><circle cx="5" cy="5" r="4.2" fill="none" stroke="#f5a524" stroke-width="1.1"/><path d="M3 5.1 L4.6 6.6 L8.6 2.2" fill="none" stroke="#f5a524" stroke-width="1.2"/></svg>
        solves problems with a positive solution first mindset</li>
      <li style="top:179px;line-height:16px">
        <svg viewBox="0 0 10 10"><circle cx="5" cy="5" r="4.2" fill="none" stroke="#f5a524" stroke-width="1.1"/><path d="M3 5.1 L4.6 6.6 L8.6 2.2" fill="none" stroke="#f5a524" stroke-width="1.2"/></svg>
        pays attention to every detail because in luxury the small<br>things are the big things</li>
    </ul>
    <svg class="footer-wave" viewBox="0 0 544 90" preserveAspectRatio="none"><path d="M0 69 C10 48 28 40 51 37 L544 0 L544 90 L0 90 Z" fill="#fff"/></svg>
    <div class="apply">Apply<br>Now!</div>
    <p class="connect">link in bio or DM to connect</p>
    <p class="website">www.ridgelanebuilders.com</p>
  </section>
</main>
</body>
</html>
```